Crintle Homes from US$9,995– Making buying a house as easy as ordering a pizza online - worldwide

I am after a website that is fun and interactive.

Buying a house should be as simple as buying a Pizza delivery online.....

Margherita 20' ………………………………………….US$9,995
Standard, 30sqm Studio with kitchen & Bathroom, Flat Roof
Four Cheese 20' ………………………………………….US$11,995
Standard, 30sqm Studio with kitchen & Bathroom, Pitched Roof
Supreme 40' ………………………………………….US$18,995
Standard, 60sqm, 2 Bedrooms, Lounge, kitchen & Bathroom, Flat Roof
Pepperoni 40' ………………………………………….US$20,995
Standard, 60sqm, 2 Bedrooms, Lounge, kitchen & Bathroom, Pitched Roof
Hawaiian 40' ………………………………………….US$22,995
Beach design, 60sqm, 2 Bedrooms, Lounge, kitchen & Bathroom, Pitched Roof
The Works 40' ………………………………………….US$24,995
Beach design, 60sqm, 2 Bedrooms, Lounge, kitchen, Bathroom, Deck, Pitched Roof

eg. https://www.dishorbit.com.au/ https://www.crustvane.com

I want a fun design....

i want to reinvent how people DESIGN - BUILD and DELIVER housing

I want a SaaS solution for drop shipping pre-built houses.

The main campaign, we are offering 1,000 homes (to anywhere in the world) for US$9,995 + shipping

Just need to Pay a Fully refundable $100 Deposit to pre-register (so need a shopping cart & payment solution).

"Queue Jumper" - pay in full and jump the queue to get your Crintle months earlier.

The campaign is based on crowdsourcing - we need 1000 participants to pre-register - then everyone's orders will be filled .

The design is very simple...
HEADER
- The Story
- The Product
- Design our Own
- Pre-Register
- Contact Us

- Login
- Shopping Cart

FOOTER
- Privacy
- Terms & Conditions
- Investment
- Media
- NGO/Government
- Contact
- Sitemap

The important parts is that everyone who
- Subscribes
- Makes Contact
- Pre-registers
…in the system automatically gets an account (just need name and email address).
The user is then sent an email with details on how they can log back in at any time and see purchases, update profile (eg. Shipping address, contact details, etc....)

This data also needs to be sent to a CRM eg Leadmoor for marketing to automate regular updates to all users.

It also needs to link to Facebook, LinkedIn , TikTok, Instagram, Twitter

You can get sample content from our old website https://tenvaledwellings.webplotter.com/ - Plus I have attached updated content in this Brief.

The hero image should be a slider with videos and images with links to "Call to Action"

PLEASE NOTE: that "crintle" is a brand new product that we pre build offsite so when it is delivered, it is ready to move in to. So we need a whole new look and a new style

This is a wordpress site to be hosted on my server - Once completed I need full access to add, amend and update any pages, images products

I am very open to different colours - do not be limited by the colours in the logo.

I would be interested to see what you can do with NO white backgrounds. (This might look good or could look horrible)

And most importantly what will your design look like on mobile devices (phones / ipads)

SUCCESS (1) is getting the user to LOOK - DREAM - BUY (Or at least pre-register)

SUCCESS (2) it MUST look fun but still highly professional and TRUSTWORTHY to get the interest of investors to invest millions $$$$$

SUCCESS (3) we need to get "Inflencers / Bloggers" talking about Crintle - this could be done by a campaign to get a million likes and get a FREE home fo both the follower and the blogger

Target Market(s)

New home buyers (younger demographic), Families wanting to extend (middle aged)

Industry/Entity Type

Housing, Crowdsourcing, Drop shipping, SaaS technology

Coding

Coded - Design and coding required

Colors
0054AA
0677BA
7BADD7
CADEEF
E8F1F8
EE7325
F08F49
F5BC92
FAE3D3
FDF4ED

Requirements
Must have
• ecommerce, user accounts, social media & crm connections for crowdsourcing marketing, Call to actions
Nice to have
• $1,000,000
Should not have
• Do NOT complicate the funnel in the steps to sign-up

```html
<!DOCTYPE html>
<html lang="en">
<head>
<meta charset="utf-8">
<title>Crintle Homes</title>
<link rel="stylesheet" href="https://fonts.googleapis.com/css2?family=Poppins:wght@400;500;600;700;800&display=swap">
<style>
:root{
  --blue:#0054AA;
  --blue-mid:#2a69b5;
  --blue-soft:#7BADD7;
  --blue-pale:#CADEEF;
  --blue-mist:#E8F1F8;
  --orange:#EE7325;
  --orange-soft:#F08F49;
  --ink:#1d2430;
  --grey:#5b6472;
  --panel:#eef1f5;
  --white:#ffffff;
}
*{margin:0;padding:0;box-sizing:border-box}
html,body{width:1200px;height:3252px;overflow:hidden}
body{font-family:"Poppins",sans-serif;color:var(--ink);background:var(--white);position:relative}
section,header,footer{position:absolute;left:0;width:1200px}
.btn{display:inline-flex;align-items:center;justify-content:center;border-radius:30px;font-weight:600;font-size:15px}

/* header */
.site-header{top:0;height:88px;background:var(--white);display:flex;align-items:center;padding:0 44px;justify-content:space-between}
.brand{display:flex;flex-direction:column}
.brand-name{font-size:36px;font-weight:800;color:var(--blue);letter-spacing:1px;line-height:1}
.brand-tag{font-size:10px;font-weight:500;color:var(--blue);letter-spacing:3px;margin-top:4px}
.main-nav{display:flex;align-items:center;gap:38px;font-size:14px;font-weight:600;color:var(--ink)}
.main-nav .active{color:var(--blue);border-bottom:2px solid var(--blue);padding-bottom:4px}
.nav-cta{background:var(--blue);color:var(--white);padding:13px 24px}

/* hero */
.hero{top:88px;height:472px}
.hero-media{position:absolute;inset:0;background:linear-gradient(180deg,#8fa7bd 0%,#c9d5df 40%,#6f7d6a 78%,#3f4d38 100%)}
.hero-shade{position:absolute;inset:0;background:linear-gradient(90deg,rgba(10,25,45,.6) 0%,rgba(10,25,45,.2) 55%,rgba(0,0,0,0) 100%)}
.hero-copy{position:absolute;left:56px;top:60px;width:460px;color:var(--white)}
.hero-copy h1{font-size:42px;font-weight:700;letter-spacing:1px;line-height:1.15}
.hero-tag{font-size:14px;font-weight:600;letter-spacing:6px;margin:10px 0 16px}
.hero-copy p{font-size:15px;line-height:1.55}
.hero-copy .btn{background:var(--blue);color:var(--white);padding:14px 26px;margin-top:32px}
.hero-dots{position:absolute;left:0;right:0;bottom:22px;display:flex;justify-content:center;gap:8px}
.hero-dots span{width:10px;height:10px;border-radius:50%;background:rgba(255,255,255,.55)}
.hero-dots span.on{background:var(--orange)}

/* lead form */
.lead{top:560px;height:220px}
.lead svg{position:absolute;inset:0}
.lead h2{position:relative;text-align:center;color:var(--white);font-size:32px;font-weight:700;padding-top:26px}
.lead-form{position:relative;display:flex;gap:24px;justify-content:center;margin-top:26px}
.field{height:52px;border-radius:30px;background:var(--white);display:flex;align-items:center;padding-left:22px;font-size:13px;color:var(--grey);width:228px}
.lead-form .submit{background:var(--orange);color:var(--white);width:220px;height:52px;letter-spacing:1px}

/* why */
.why{top:800px;height:420px}
.section-title{text-align:center;font-size:38px;font-weight:700;color:var(--ink)}
.rule{width:70px;height:3px;background:var(--orange);margin:12px auto 0}
.why-cards{position:absolute;top:90px;left:0;right:0;display:flex;justify-content:center;gap:80px;align-items:flex-start}
.why-card{width:250px;text-align:center;padding:30px 18px 20px}
.why-card.featured{background:var(--blue);color:var(--white);width:312px;height:270px;box-shadow:0 10px 24px rgba(0,84,170,.25)}
.why-card svg{width:82px;height:82px}
.why-card h3{font-size:16px;font-weight:700;margin:14px 0 10px;text-transform:uppercase}
.why-card p{font-size:13px;line-height:1.5;color:var(--grey)}
.why-card.featured p{color:var(--white)}
.arrow{position:absolute;width:34px;height:34px;border-radius:50%;display:flex;align-items:center;justify-content:center}
.arrow.light{background:#c9ced6}
.arrow.dark{background:var(--blue)}

/* about */
.about{top:1240px;height:500px}
.about svg.bg{position:absolute;inset:0}
.about-inner{position:relative;text-align:center;color:var(--white);padding-top:80px}
.about-inner h2{font-size:38px;font-weight:700}
.about-inner .rule{background:var(--white)}
.about-inner p{width:870px;margin:26px auto 0;font-size:15px;line-height:1.7}
.about-actions{display:flex;justify-content:center;gap:18px;margin-top:34px}
.about-actions .btn{width:148px;height:52px}
.btn-white{background:var(--white);color:var(--blue)}
.btn-outline{border:2px solid var(--white);color:var(--white)}

/* team */
.team{top:1770px;height:400px}
.team-grid{position:absolute;top:110px;left:112px;display:flex;gap:80px}
.member{width:180px;height:200px;border:2px solid var(--blue);border-radius:6px;text-align:center;padding-top:14px;background:var(--white)}
.portrait{width:92px;height:92px;border-radius:50%;margin:0 auto;background:linear-gradient(160deg,#9ab3cc,#4f6f92);border:3px solid var(--blue-pale)}
.member h4{font-size:16px;font-weight:700;margin-top:10px}
.member .role{font-size:11px;color:var(--grey)}
.socials{display:flex;justify-content:center;gap:7px;margin-top:10px}
.socials span{width:14px;height:14px;border-radius:50%;background:var(--orange)}

/* stats */
.stats{top:2170px;height:180px;display:flex;justify-content:center;gap:30px}
.stat{width:230px;text-align:center}
.stat b{display:block;font-size:54px;font-weight:700;color:var(--blue);line-height:1.1}
.stat span{font-size:14px;font-weight:500;line-height:1.4;display:block;margin-top:8px}

/* newsletter */
.newsletter{top:2420px;height:380px;background:var(--panel);text-align:center}
.newsletter .section-title{padding-top:66px}
.newsletter p{width:860px;margin:30px auto 0;font-size:15px;line-height:1.7;color:var(--ink)}
.subscribe{width:720px;height:60px;margin:34px auto 0;background:var(--white);border-radius:34px;display:flex;align-items:center;justify-content:space-between;padding-left:26px;box-shadow:0 2px 6px rgba(0,0,0,.08)}
.subscribe span{font-size:13px;color:var(--grey)}
.subscribe .btn{background:var(--orange);color:var(--white);height:60px;width:200px;border-radius:0 34px 34px 0}

/* footer */
.site-footer{top:2800px;height:452px;background:var(--blue-mid);color:var(--white)}
.foot-cols{position:absolute;top:64px;left:56px;right:56px;display:flex}
.foot-cols h5{font-size:24px;font-weight:700;margin-bottom:18px}
.contact-form{width:500px;margin-right:58px}
.row{display:flex;gap:14px;margin-bottom:12px}
.f-input{flex:1;height:32px;background:var(--white);border-radius:3px;font-size:12px;color:var(--grey);padding:8px 12px}
.f-area{height:92px}
.f-submit{background:var(--orange);color:var(--white);font-size:12px;padding:8px 20px;border-radius:20px;font-weight:600;display:inline-block}
.links{width:170px}
.links ul{list-style:none;font-size:14px;line-height:2.2}
.links li::before{content:"▸ ";font-size:11px}
.contact{width:220px}
.contact li{list-style:none;display:flex;gap:10px;align-items:flex-start;font-size:13px;margin-bottom:16px;line-height:1.4}
.contact i{flex:none;width:26px;height:26px;border-radius:50%;background:var(--orange);display:flex;align-items:center;justify-content:center}
.foot-base{position:absolute;left:56px;right:56px;bottom:28px;border-top:1px solid rgba(255,255,255,.35);padding-top:16px;text-align:center;font-size:12px}
</style>
</head>
<body>

<header class="site-header">
  <div class="brand">
    <span class="brand-name">CRINTLE</span>
    <span class="brand-tag">DESIGN · BUILD · DELIVER</span>
  </div>
  <nav class="main-nav">
    <span class="active">HOME</span>
    <span>THE STORY</span>
    <span>THE PRODUCT</span>
    <span>PRE-REGISTER</span>
    <span class="btn nav-cta">CONTACT US</span>
    <svg width="24" height="22" viewBox="0 0 24 22"><path d="M1 2h4l3 12h12l3-9H7" fill="none" stroke="#1d2430" stroke-width="2"/><circle cx="10" cy="19" r="2" fill="#1d2430"/><circle cx="19" cy="19" r="2" fill="#1d2430"/></svg>
  </nav>
</header>

<section class="hero">
  <div class="hero-media" role="img" aria-label="Photo of a modern two-storey prefabricated house with a lawn under an evening sky"></div>
  <div class="hero-shade"></div>
  <div class="hero-copy">
    <h1>WELCOME TO CRINTLE</h1>
    <div class="hero-tag">DESIGN - BUILD - DELIVER</div>
    <p>The main campaign, we are offering 1,000 homes (to anywhere in the world) for US$9,995 + shipping. Just need to Pay a Fully refundable $100 Deposit to pre-register.</p>
    <span class="btn">Get Started</span>
  </div>
  <div class="hero-dots"><span></span><span class="on"></span><span></span><span></span></div>
</section>

<section class="lead">
  <svg width="1200" height="220" viewBox="0 0 1200 220" preserveAspectRatio="none"><path d="M0 0H1200V170Q600 240 0 170Z" fill="#2a69b5"/></svg>
  <h2>GET YOUR FREE CRINTLE</h2>
  <div class="lead-form">
    <span class="field">Name</span>
    <span class="field">Email</span>
    <span class="field">Phone Number</span>
    <span class="btn submit">SUBMIT</span>
  </div>
</section>

<section class="why">
  <h2 class="section-title">WHY CHOOSE US?</h2>
  <div class="rule"></div>
  <div class="why-cards">
    <div class="why-card">
      <svg viewBox="0 0 80 80"><path d="M10 56A30 30 0 1 1 70 56" fill="none" stroke="#1d2430" stroke-width="4"/><path d="M40 50L56 30" stroke="#EE7325" stroke-width="4" stroke-linecap="round"/><circle cx="40" cy="50" r="5" fill="#1d2430"/><path d="M20 30l4 3M40 20v5M60 30l-4 3" stroke="#1d2430" stroke-width="3"/></svg>
      <h3>Fast Construction</h3>
      <p>From the time the contract is signed and deposit is paid - we can have you living in your new house in under 12 weeks.</p>
    </div>
    <div class="why-card featured">
      <svg viewBox="0 0 80 80"><circle cx="40" cy="24" r="12" fill="none" stroke="#fff" stroke-width="3"/><path d="M40 17v14M36 20h6a3 3 0 0 1 0 4h-4a3 3 0 0 0 0 4h6" fill="none" stroke="#fff" stroke-width="2"/><path d="M8 58l14-10h14l10 6h-14M22 48l-6 16M46 54l18-10 6 4-24 16H22" fill="none" stroke="#fff" stroke-width="3" stroke-linejoin="round"/></svg>
      <h3>Affordable</h3>
      <p>You can own your own home from under $10K per week. You supply the land - we will supply the house.</p>
    </div>
    <div class="why-card">
      <svg viewBox="0 0 80 80"><path d="M40 8l5 10 11 1-8 7 2 11-10-6-10 6 2-11-8-7 11-1z" fill="none" stroke="#EE7325" stroke-width="3"/><path d="M18 24l3 6 7 1-5 4 1 7-6-4-6 4 1-7-5-4 7-1zM62 24l3 6 7 1-5 4 1 7-6-4-6 4 1-7-5-4 7-1z" fill="none" stroke="#EE7325" stroke-width="2.5"/><path d="M22 74V56l8-10h4v10h16a4 4 0 0 1 0 8M22 74h24a4 4 0 0 0 4-4" fill="none" stroke="#1d2430" stroke-width="3"/></svg>
      <h3>10 Year Guarantee</h3>
      <p>Australian regulations require builders to give a 7 year builders warranty. We are so confident in our structures.</p>
    </div>
  </div>
  <span class="arrow light" style="left:30px;top:240px"><svg width="14" height="14"><path d="M9 2L4 7l5 5" fill="none" stroke="#fff" stroke-width="2.5"/></svg></span>
  <span class="arrow dark" style="right:30px;top:240px"><svg width="14" height="14"><path d="M5 2l5 5-5 5" fill="none" stroke="#fff" stroke-width="2.5"/></svg></span>
</section>

<section class="about">
  <svg class="bg" width="1200" height="500" viewBox="0 0 1200 500" preserveAspectRatio="none" role="img" aria-label="Blue background with faint architectural plan">
    <defs><linearGradient id="aboutFill" x1="0" y1="0" x2="1" y2="1"><stop offset="0" stop-color="#2a69b5"/><stop offset="1" stop-color="#3a7cc6"/></linearGradient></defs>
    <path d="M0 30Q600 -20 1200 30V470Q600 520 0 470Z" fill="url(#aboutFill)"/>
  </svg>
  <div class="about-inner">
    <h2>ABOUT CRINTLE</h2>
    <div class="rule"></div>
    <p>As a company dedicated to providing premier customer service, it is important to us to deliver unparalleled workmanship on every assignment. We are committed, licensed, bonded, and insured. With our experience and expertise, we can provide the support your project deserves.</p>
    <p>We will work with you to meet deadlines and coordinate with other related projects. We will maintain open communication with you to keep you up to date on the status of your job. We do this to guarantee that the project is completed according to your preferences.</p>
    <div class="about-actions"><span class="btn btn-white">Read More</span><span class="btn btn-outline">Pre-Register</span></div>
  </div>
</section>

<section class="team">
  <h2 class="section-title">OUR TEAM</h2>
  <div class="rule"></div>
  <div class="team-grid">
    <div class="member"><div class="portrait" role="img" aria-label="Portrait photo of Marlo Penn"></div><h4>Marlo Penn</h4><div class="role">Builder (Co-Founder)</div><div class="socials"><span></span><span></span><span></span><span></span></div></div>
    <div class="member"><div class="portrait" role="img" aria-label="Portrait photo of Tavin Reyes"></div><h4>Tavin Reyes</h4><div class="role">Architect</div><div class="socials"><span></span><span></span><span></span><span></span></div></div>
    <div class="member"><div class="portrait" role="img" aria-label="Portrait photo of Ilsa Dorran"></div><h4>Ilsa Dorran</h4><div class="role">Structural Engineer</div><div class="socials"><span></span><span></span><span></span><span></span></div></div>
    <div class="member"><div class="portrait" role="img" aria-label="Portrait photo of Bram Keller"></div><h4>Bram Keller</h4><div class="role">Plumbing Engineer</div><div class="socials"><span></span><span></span><span></span><span></span></div></div>
  </div>
  <span class="arrow light" style="left:30px;top:190px"><svg width="14" height="14"><path d="M9 2L4 7l5 5" fill="none" stroke="#fff" stroke-width="2.5"/></svg></span>
  <span class="arrow dark" style="right:30px;top:190px"><svg width="14" height="14"><path d="M5 2l5 5-5 5" fill="none" stroke="#fff" stroke-width="2.5"/></svg></span>
</section>

<section class="stats">
  <div class="stat"><b>10+</b><span>Over a Decade of Experience</span></div>
  <div class="stat"><b>99.9%</b><span>Hundreds of Happy Clients with 99.9% Success Rate</span></div>
  <div class="stat"><b>7 yr</b><span>Built on 7 Years of Warranty</span></div>
  <div class="stat"><b>100%</b><span>Licensed Contractors &amp; On-Time Completion</span></div>
</section>

<section class="newsletter">
  <h2 class="section-title">JOIN OUR NEWSLETTER</h2>
  <div class="rule"></div>
  <p>We combine our industry knowledge, the highest quality building supplies and equipment, and our dedication to deliver exceptional service to our clients. We will stay in touch, keeping you up to date on both the paperwork and renovation process.</p>
  <div class="subscribe"><span>Enter The Email</span><span class="btn">Subscribe</span></div>
</section>

<footer class="site-footer">
  <div class="foot-cols">
    <div class="contact-form">
      <h5>Get In Touch:</h5>
      <div class="row"><span class="f-input">Name</span><span class="f-input">Phone</span></div>
      <div class="row"><span class="f-input">Email</span></div>
      <div class="row"><span class="f-input f-area">Message</span></div>
      <span class="f-submit">SUBMIT</span>
    </div>
    <div class="links">
      <h5>Quick Link</h5>
      <ul><li>Home</li><li>Story</li><li>Product</li><li>Testimonials</li><li>Our Team</li><li>Contact us</li></ul>
    </div>
    <div class="links">
      <h5>Help Link</h5>
      <ul><li>Media</li><li>Sitemap</li><li>Privacy</li><li>Investment</li><li>Contact</li><li>Terms &amp; Conditions</li></ul>
    </div>
    <div class="contact">
      <h5>Contact us</h5>
      <ul>
        <li><i><svg width="12" height="14" viewBox="0 0 12 14"><path d="M6 13S1 8 1 5a5 5 0 0 1 10 0c0 3-5 8-5 8z" fill="#fff"/><circle cx="6" cy="5" r="2" fill="#EE7325"/></svg></i>PO 218, Harlow Vale, Victoria, 3790, Australia</li>
        <li><i><svg width="12" height="12" viewBox="0 0 12 12"><path d="M2 1h3l1 3-2 1a7 7 0 0 0 3 3l1-2 3 1v3a1 1 0 0 1-1 1A10 10 0 0 1 1 2a1 1 0 0 1 1-1z" fill="#fff"/></svg></i>(04) 555 0192</li>
        <li><i><svg width="12" height="10" viewBox="0 0 12 10"><rect x="0.5" y="0.5" width="11" height="9" fill="#fff"/><path d="M1 1l5 4 5-4" fill="none" stroke="#EE7325"/></svg></i>info@crintle.com</li>
      </ul>
    </div>
  </div>
  <div class="foot-base">Copyright©2023 Crintle All Rights Reserved.</div>
</footer>

</body>
</html>
```